Velvet Basin Suites, a portable luxury restroom trailer company needs a landing page

We need a landing page for a luxury portable restroom trailer company. This should be modern, and simple - use any combination of Pantone colors: Warm Gray 1C, Black 7C, 7529c, 873C, 8003C

We rent these trailers for special events like weddings, private parties, festivals, family reunions, team building, wine tastings, beer tastings, food truck round-ups, etc.

An idea of the landing page is in the files below. Please use stock photography and placeholder text for now. The winning design will be given final content.

Requirements
Must have
• Multiple "Get Quote" buttons or a place for them to type in type of rental, how many people etc

```html
<!DOCTYPE html>
<html lang="en">
<head>
<meta charset="utf-8">
<title>Velvet Basin Suites — Luxury Portable Restroom Trailers</title>
<link rel="stylesheet" href="https://fonts.googleapis.com/css2?family=Lora:wght@400;500&family=Roboto:wght@400;500;700&display=swap">
<style>
:root{
  --ink:#3d3935;
  --bronze:#8a6c45;
  --taupe:#b3a695;
  --warm-gray:#d7d2cb;
  --mist:#f7f7f7;
  --white:#ffffff;
  --body:#4a4642;
  --muted:#6d6863;
}
*{box-sizing:border-box;margin:0;padding:0}
html,body{width:1200px;height:4435px;overflow:hidden}
body{position:relative;background:var(--white);font-family:"Roboto",Arial,sans-serif;color:var(--body)}
.abs{position:absolute}
.serif{font-family:"Lora",Georgia,serif;color:#111}

/* header */
.site-header{left:0;top:0;width:1200px;height:93px;background:var(--white);z-index:3}
.brand{left:120px;top:26px;display:flex;align-items:center;gap:8px;font-family:"Roboto",Arial,sans-serif;font-size:13px;font-weight:500;color:var(--bronze);letter-spacing:.5px}
.brand-dot{width:14px;height:14px;border-radius:50%;background:var(--bronze)}
.main-nav{right:122px;top:38px;display:flex;gap:38px;font-size:11px;font-weight:700;color:var(--ink);letter-spacing:.3px}

/* hero */
.hero-photo{left:0;top:93px;width:1200px;height:597px;background:linear-gradient(90deg,rgba(255,255,255,.95) 0%,rgba(255,255,255,.55) 25%,rgba(255,255,255,0) 45%),linear-gradient(180deg,#6f7d55 0%,#a3a886 35%,#dfe0da 55%,#8a9a5c 80%,#6c7b3f 100%)}
.hero-title{left:120px;top:168px;font-size:55px;line-height:72px;font-weight:500}
.hero-copy{left:121px;top:318px;width:440px;font-size:14px;line-height:17px;color:#222}
.btn{display:flex;align-items:center;justify-content:center;height:38px;font-size:10px;font-weight:700;letter-spacing:.4px}
.btn-dark{background:var(--ink);color:var(--white)}
.btn-light{background:var(--white);color:var(--ink)}
.hero-dots{left:572px;top:597px;display:flex;gap:14px}
.hero-dots span{width:10px;height:10px;border-radius:50%;background:rgba(255,255,255,.6)}
.hero-dots span:first-child{background:var(--white)}
.hero-curve{left:0;top:620px;width:1200px;height:80px}

/* section headings */
.section-title{left:0;width:1200px;text-align:center;font-size:46px;font-weight:400}
.rule{height:6px;background:var(--bronze)}
.rule-left{clip-path:polygon(0 50%,100% 0,100% 100%)}
.rule-right{clip-path:polygon(0 0,100% 50%,0 100%)}

/* about */
.about-blob{left:55px;top:865px;width:400px;height:385px}
.about-text{left:541px;top:940px;width:538px;font-size:14.5px;line-height:22.6px;color:#333}

/* events */
.events-bg{left:0;top:1260px;width:1200px;height:760px}
.event-card{width:228px}
.event-photo{width:228px;height:164px;border-radius:22px}
.event-name{margin-top:28px;font-size:22px}
.event-copy{margin-top:20px;font-size:11px;line-height:17px;color:var(--muted)}
.event-card .btn{margin-top:40px;width:127px}
.slider-arrow{top:1640px;font-size:26px;color:#111}

/* products */
.product-photo{width:352px;height:200px;border-radius:28px}
.product-name{font-size:22px}
.product-copy{width:510px;font-size:11px;line-height:17px;color:var(--muted)}
.read-more{display:flex;align-items:center;gap:10px;font-size:13px;font-weight:700;color:#222;letter-spacing:.3px}

/* contact */
.field{height:38px;background:var(--mist);display:flex;align-items:center;justify-content:space-between;padding:0 14px;font-size:11px;color:#333}
.field-active{background:var(--white);border:1.5px solid var(--bronze);border-radius:2px}
.field-label{font-size:10px;color:#333}

/* footer */
.footer-curve{left:0;top:4010px;width:1200px;height:80px}
.site-footer{left:0;top:4085px;width:1200px;height:350px;background:var(--ink)}
.footer-head{font-family:"Lora",Georgia,serif;font-size:22px;color:var(--white);letter-spacing:1px}
.footer-links{list-style:none;font-size:10.5px;color:var(--white);line-height:32.8px;letter-spacing:.3px}
.social{display:flex;gap:28px}
.social span{width:30px;height:30px;border-radius:50%;border:2.5px solid var(--white)}
.copyright{left:0;top:4402px;width:1200px;text-align:center;font-size:10.5px;color:var(--white)}
</style>
</head>
<body>

<header class="abs site-header">
  <div class="abs brand"><span class="brand-dot"></span>Velvet Basin Suites</div>
  <nav class="abs main-nav"><span>HOME</span><span>ABOUT</span><span>EVENTS</span><span>PRODUCTS</span><span>CONTACT</span></nav>
</header>

<!-- hero -->
<div class="abs hero-photo" role="img" aria-label="Luxury camper trailer parked on a grassy field with friends relaxing in camp chairs"></div>
<h1 class="abs serif hero-title">Luxury Portable<br>Restroom Trailer</h1>
<p class="abs hero-copy">Lorem ipsum dolor sit amet, consectetur adipiscing elit. Pretium ultrices in dolor venenatis odio.</p>
<div class="abs btn btn-dark" style="left:120px;top:418px;width:127px">CONTACT US</div>
<div class="abs btn btn-light" style="left:275px;top:418px;width:127px">PRODUCTS</div>
<div class="abs hero-dots"><span></span><span></span><span></span></div>
<svg class="abs hero-curve" viewBox="0 0 1200 80" preserveAspectRatio="none">
  <path d="M0 20 Q600 70 1200 20 L1200 80 L0 80 Z" fill="#fff"/>
  <path d="M0 20 Q600 90 1200 20 Q600 58 0 20 Z" fill="#8a6c45"/>
</svg>

<!-- about -->
<div class="abs rule rule-left" style="left:240px;top:815px;width:230px"></div>
<h2 class="abs serif section-title" style="top:788px">About Us</h2>
<div class="abs rule rule-right" style="left:730px;top:815px;width:230px"></div>
<svg class="abs about-blob" viewBox="0 0 400 385" role="img" aria-label="Friends gathered with a guitar beside a camper trailer, framed in layered organic shapes">
  <path d="M30 55 C70 20 160 60 200 120 C250 200 260 330 170 370 C90 400 10 330 5 230 C0 160 0 80 30 55Z" fill="#d7d2cb"/>
  <path d="M90 40 C170 -10 330 10 390 110 C430 200 370 340 250 375 C150 400 60 330 45 220 C35 140 40 70 90 40Z" fill="#b3a695"/>
  <circle cx="210" cy="185" r="152" fill="#7b8a5a"/>
</svg>
<p class="abs about-text">Lorem ipsum dolor sit amet, consectetur adipiscing elit. Felis convallis dictumst risus, leo. Erat mauris, dolor sed eu. Ante lacus at at erat ultrices feugiat aliquam augue dapibus. Tellus, commodo est augue nam amet in. Sit nibh ante bibendum hac volutpat elementum mattis. Duis convallis sem proin posuere. Vitae velit cursus nec neque nibh condimentum. Nunc orci eu dolor porttitor neque, nisl et. Ipsum maecenas quis aenean arcu nec, sed vulputate nunc. Nec purus pharetra ipsum in nibh nam arcu ac. Vel a est mauris hac sed dui ultrices. Tortor nulla porttitor neque, scelerisque vitae scelerisque. Nullam accumsan, vulputate enim, consequat.<br>Mattis sed aenean sit sed arcu viverra lorem diam. Odio sit nunc.</p>

<!-- events -->
<svg class="abs events-bg" viewBox="0 0 1200 760" preserveAspectRatio="none">
  <path d="M0 120 C300 80 500 30 800 15 C1000 5 1150 40 1200 60 L1200 700 C1000 760 700 740 400 720 C200 710 60 740 0 680 Z" fill="#f7f7f7"/>
</svg>
<div class="abs rule rule-left" style="left:265px;top:1371px;width:230px"></div>
<h2 class="abs serif section-title" style="top:1344px">Events</h2>
<div class="abs rule rule-right" style="left:705px;top:1371px;width:230px"></div>
<div class="abs slider-arrow" style="left:58px">&#8249;</div>
<div class="abs slider-arrow" style="left:1128px">&#8250;</div>

<article class="abs event-card" style="left:120px;top:1472px">
  <div class="event-photo" role="img" aria-label="Guests raising glasses of red wine" style="background:linear-gradient(135deg,#5a2e3a,#c89a8c 55%,#6e3a40)"></div>
  <h3 class="serif event-name">Wine Tasting</h3>
  <p class="event-copy">Lorem ipsum dolor sit amet, consectetur adipiscing elit. Felis convallis dictumst risus, leo. Erat mauris, dolor sed eu. Ante lacus at at erat ultrices feugiat aliquam augue dapibus. Tellus, commodo est augue nam amet in.</p>
  <div class="btn btn-dark">VIEW MORE</div>
</article>
<article class="abs event-card" style="left:363px;top:1472px">
  <div class="event-photo" role="img" aria-label="Bridal party celebrating outdoors with balloons" style="background:linear-gradient(180deg,#4f6a3c,#d9cfc7 60%,#8c9a6e)"></div>
  <h3 class="serif event-name">Wedding Party</h3>
  <p class="event-copy">Lorem ipsum dolor sit amet, consectetur adipiscing elit. Felis convallis dictumst risus, leo. Erat mauris, dolor sed eu. Ante lacus at at erat ultrices feugiat aliquam augue dapibus. Tellus, commodo est augue nam amet in.</p>
  <div class="btn btn-dark">VIEW MORE</div>
</article>
<article class="abs event-card" style="left:606px;top:1472px">
  <div class="event-photo" role="img" aria-label="Colourful party balloons" style="background:linear-gradient(120deg,#2b8a8a,#e0c24a 40%,#d0506a 70%,#5a9ad0)"></div>
  <h3 class="serif event-name">Birthday Party</h3>
  <p class="event-copy">Lorem ipsum dolor sit amet, consectetur adipiscing elit. Felis convallis dictumst risus, leo. Erat mauris, dolor sed eu. Ante lacus at at erat ultrices feugiat aliquam augue dapibus. Tellus, commodo est augue nam amet in.</p>
  <div class="btn btn-dark">VIEW MORE</div>
</article>
<article class="abs event-card" style="left:849px;top:1472px">
  <div class="event-photo" role="img" aria-label="Friends chatting at a garden party" style="background:linear-gradient(160deg,#2f4a2a,#6f8a55 55%,#c9c1b4)"></div>
  <h3 class="serif event-name">Private Party</h3>
  <p class="event-copy">Lorem ipsum dolor sit amet, consectetur adipiscing elit. Felis convallis dictumst risus, leo. Erat mauris, dolor sed eu. Ante lacus at at erat ultrices feugiat aliquam augue dapibus. Tellus, commodo est augue nam amet in.</p>
  <div class="btn btn-dark">VIEW MORE</div>
</article>

<!-- products -->
<svg class="abs" style="left:0;top:2200px;width:1200px;height:1080px" viewBox="0 0 1200 1080" preserveAspectRatio="none">
  <path d="M1200 40 C1000 120 820 220 700 340 C560 480 420 560 200 600 C80 620 20 700 60 820 C120 980 400 1060 700 1040 C950 1020 1150 900 1200 760 Z" fill="#f7f7f7"/>
</svg>
<div class="abs rule rule-left" style="left:195px;top:2161px;width:230px"></div>
<h2 class="abs serif section-title" style="top:2134px">Our Products</h2>
<div class="abs rule rule-right" style="left:775px;top:2161px;width:230px"></div>

<h3 class="abs serif product-name" style="left:120px;top:2268px">The Elite</h3>
<p class="abs product-copy" style="left:120px;top:2325px">Lorem ipsum dolor sit amet, consectetur adipiscing elit. Felis convallis dictumst risus, leo. Erat mauris, dolor sed eu. Ante lacus at at erat ultrices feugiat aliquam augue dapibus. Tellus, commodo est augue nam amet in.</p>
<div class="abs read-more" style="left:120px;top:2410px">READ MORE <svg width="30" height="10" viewBox="0 0 30 10"><path d="M0 5H28M23 1L28 5L23 9" stroke="#222" fill="none" stroke-width="1.3"/></svg></div>
<div class="abs product-photo" style="left:727px;top:2247px;background:linear-gradient(180deg,#3a4a2e,#b98a54 45%,#e8e4dc 70%,#5d6b3a)" role="img" aria-label="Vintage wood-panelled trailer with open awning"></div>

<div class="abs product-photo" style="left:120px;top:2500px;background:linear-gradient(180deg,#2d4a66,#6d88a0 45%,#d8b88a 70%,#3d3a30)" role="img" aria-label="Polished trailer glowing at dusk with a parasol and seating"></div>
<h3 class="abs serif product-name" style="left:551px;top:2521px">The Embassy</h3>
<p class="abs product-copy" style="left:551px;top:2578px">Lorem ipsum dolor sit amet, consectetur adipiscing elit. Felis convallis dictumst risus, leo. Erat mauris, dolor sed eu. Ante lacus at at erat ultrices feugiat aliquam augue dapibus. Tellus, commodo est augue nam amet in.</p>
<div class="abs read-more" style="left:551px;top:2663px">READ MORE <svg width="30" height="10" viewBox="0 0 30 10"><path d="M0 5H28M23 1L28 5L23 9" stroke="#222" fill="none" stroke-width="1.3"/></svg></div>

<h3 class="abs serif product-name" style="left:120px;top:2774px">The Villa</h3>
<p class="abs product-copy" style="left:120px;top:2831px">Lorem ipsum dolor sit amet, consectetur adipiscing elit. Felis convallis dictumst risus, leo. Erat mauris, dolor sed eu. Ante lacus at at erat ultrices feugiat aliquam augue dapibus. Tellus, commodo est augue nam amet in.</p>
<div class="abs read-more" style="left:120px;top:2916px">READ MORE <svg width="30" height="10" viewBox="0 0 30 10"><path d="M0 5H28M23 1L28 5L23 9" stroke="#222" fill="none" stroke-width="1.3"/></svg></div>
<div class="abs product-photo" style="left:727px;top:2753px;background:linear-gradient(180deg,#cfd6dc,#9aa0a4 45%,#6e6e6a 70%,#8a7c62)" role="img" aria-label="Silver aluminium trailer parked on a gravel lot"></div>

<div class="abs product-photo" style="left:120px;top:3006px;background:linear-gradient(180deg,#6a6f4a,#e6dbe0 45%,#c9b6b8 65%,#6d5e4c)" role="img" aria-label="Pale pink caravan parked on dirt beside trees"></div>
<h3 class="abs serif product-name" style="left:551px;top:3027px">The Estate</h3>
<p class="abs product-copy" style="left:551px;top:3084px">Lorem ipsum dolor sit amet, consectetur adipiscing elit. Felis convallis dictumst risus, leo. Erat mauris, dolor sed eu. Ante lacus at at erat ultrices feugiat aliquam augue dapibus. Tellus, commodo est augue nam amet in.</p>
<div class="abs read-more" style="left:551px;top:3169px">READ MORE <svg width="30" height="10" viewBox="0 0 30 10"><path d="M0 5H28M23 1L28 5L23 9" stroke="#222" fill="none" stroke-width="1.3"/></svg></div>

<div class="abs btn btn-dark" style="left:537px;top:3302px;width:126px">VIEW ALL</div>

<!-- contact -->
<div class="abs rule rule-left" style="left:220px;top:3444px;width:230px"></div>
<h2 class="abs serif section-title" style="top:3417px">Contact Us</h2>
<div class="abs rule rule-right" style="left:750px;top:3444px;width:230px"></div>

<form>
  <label class="abs field-label" style="left:120px;top:3532px">First Name</label>
  <div class="abs field field-active" style="left:120px;top:3551px;width:459px"><span style="font-size:16px;color:#222">|</span></div>
  <div class="abs field" style="left:620px;top:3551px;width:458px">Last Name</div>

  <div class="abs field" style="left:120px;top:3612px;width:459px">Email Address</div>
  <div class="abs field" style="left:620px;top:3612px;width:458px">Phone</div>

  <div class="abs field" style="left:120px;top:3675px;width:459px">Type Of Event <svg width="10" height="6"><path d="M1 1L5 5L9 1" stroke="#333" fill="none" stroke-width="1.3"/></svg></div>
  <div class="abs field" style="left:620px;top:3675px;width:458px">How Many People <svg width="10" height="6"><path d="M1 1L5 5L9 1" stroke="#333" fill="none" stroke-width="1.3"/></svg></div>

  <div class="abs field" style="left:120px;top:3737px;width:459px">Type Of Product You Are Interested In <svg width="10" height="6"><path d="M1 1L5 5L9 1" stroke="#333" fill="none" stroke-width="1.3"/></svg></div>
  <div class="abs field" style="left:620px;top:3737px;width:458px">When Do You Need It <svg width="10" height="6"><path d="M1 1L5 5L9 1" stroke="#333" fill="none" stroke-width="1.3"/></svg></div>

  <div class="abs field" style="left:120px;top:3800px;width:459px">For How Long <svg width="10" height="6"><path d="M1 1L5 5L9 1" stroke="#333" fill="none" stroke-width="1.3"/></svg></div>
  <div class="abs field" style="left:620px;top:3800px;width:458px">Where <svg width="10" height="6"><path d="M1 1L5 5L9 1" stroke="#333" fill="none" stroke-width="1.3"/></svg></div>

  <div class="abs btn btn-dark" style="left:537px;top:3883px;width:126px;font-size:11px">Send</div>
</form>

<!-- footer -->
<svg class="abs footer-curve" viewBox="0 0 1200 80" preserveAspectRatio="none">
  <path d="M0 80 L0 70 Q600 -10 1200 70 L1200 80 Z" fill="#3d3935"/>
  <path d="M0 62 Q600 -20 1200 62 Q600 10 0 62 Z" fill="#8a6c45"/>
</svg>
<footer class="abs site-footer"></footer>
<h4 class="abs footer-head" style="left:120px;top:4140px">QUICK LINKS</h4>
<ul class="abs footer-links" style="left:120px;top:4182px"><li>HOME</li><li>ABOUT</li><li>EVENTS</li><li>PRODUCT</li><li>CONTACT</li></ul>
<h4 class="abs footer-head" style="left:522px;top:4140px">LEGAL</h4>
<ul class="abs footer-links" style="left:522px;top:4182px"><li>PRIVACY POLICY</li><li>REFUND AND RETURNS</li></ul>
<h4 class="abs footer-head" style="left:849px;top:4140px">SOCIAL &nbsp;LINKS</h4>
<div class="abs social" style="left:850px;top:4200px"><span></span><span></span><span></span></div>
<p class="abs copyright">Copyright Northwind Studio 2021 - Legal</p>

</body>
</html>
```